Product flyer with pricing

We manufacture iconic and luxury vending trailers. for our first trailer we need a flyer created to give to prospective clients with base pricing. I am uploading an example along with graphic files.

```html
<!DOCTYPE html>
<html lang="en">
<head>
<meta charset="utf-8">
<title>Prairie Cottage Mini – Flyer</title>
<link rel="stylesheet" href="https://fonts.googleapis.com/css2?family=Oswald:wght@400;500;600;700&family=Open+Sans:wght@400;600;700&display=swap">
<style>
  :root{
    --green:#2f7d1e;
    --green-dark:#1d5c12;
    --green-light:#a9d98c;
    --gold:#e0a300;
    --gold-dark:#b98200;
    --yellow:#f7d511;
    --ink:#2b2b2b;
    --white:#ffffff;
    --charcoal:#1c1c1c;
  }
  *{box-sizing:border-box;margin:0;padding:0}
  html,body{width:720px;height:1200px;overflow:hidden;background:#fff}
  .flyer{position:relative;width:720px;height:1200px;overflow:hidden;background:linear-gradient(180deg,#fff 0%,#fafafa 60%,#f2f2f2 100%);font-family:"Open Sans",Arial,sans-serif;color:var(--ink)}
  .backdrop{position:absolute;inset:0}
  .brand{position:absolute;left:66px;top:150px;width:220px;display:flex;align-items:center;gap:10px}
  .brand-dot{width:22px;height:22px;border-radius:50%;background:var(--gold);flex:none}
  .brand-name{font-family:"Oswald",sans-serif;font-weight:600;font-size:24px;line-height:1.05;color:var(--green);text-transform:uppercase}
  .photo{position:absolute;overflow:hidden}
  .photo-hero{left:350px;top:-120px;width:500px;height:500px;border-radius:50%;border:5px solid var(--gold);background:linear-gradient(160deg,#6d93c9 0%,#9bb3c9 30%,#e9ecef 55%,#c7c9cb 75%,#6c6e70 100%)}
  .photo-round{border-radius:50%;border:5px solid var(--green-light)}
  .photo-window{left:395px;top:325px;width:300px;height:300px;background:linear-gradient(170deg,#8aa8cf 0%,#eef0f2 35%,#dfe2e5 60%,#6a6d70 85%,#3f4144 100%)}
  .photo-side{left:220px;top:447px;width:200px;height:200px;background:linear-gradient(175deg,#7ea3d4 0%,#f1f3f5 40%,#d8dbde 70%,#55585b 100%)}
  .photo-rear{left:40px;top:456px;width:190px;height:190px;background:linear-gradient(175deg,#6f99d2 0%,#f4f5f6 40%,#dcdfe2 75%,#4d5053 100%)}
  .title{position:absolute;left:49px;top:262px;font-family:"Oswald",sans-serif;font-weight:700;text-transform:uppercase;line-height:1}
  .title-lead{font-size:40px;color:var(--white);letter-spacing:.5px}
  .title-lead .the{font-weight:400}
  .title-lead .quote{color:var(--yellow)}
  .title-main{font-size:66px;color:var(--yellow);margin-top:2px}
  .title-main .quote{font-size:40px}
  .subtitle{font-family:"Oswald",sans-serif;font-weight:600;font-size:22px;color:var(--white);text-transform:uppercase;margin-top:10px}
  .pill{position:absolute;height:40px;border-radius:20px;background:linear-gradient(180deg,#3c9127,var(--green-dark));color:var(--white);font-family:"Oswald",sans-serif;font-weight:500;font-size:26px;text-transform:uppercase;display:flex;align-items:center;justify-content:center}
  .pill-features{left:47px;top:677px;width:295px}
  .pill-price{left:355px;top:677px;width:328px;justify-content:flex-start;padding-left:18px}
  .price-tag{position:absolute;right:0;top:-6px;height:52px;width:178px;border-radius:26px;background:linear-gradient(180deg,#f2bb18,var(--gold-dark));display:flex;align-items:center;justify-content:center;font-size:40px;font-weight:600;color:var(--white)}
  .feature-list{position:absolute;list-style:none;font-size:15.5px;line-height:1.45}
  .feature-list li{position:relative;padding-left:32px;margin-bottom:8px}
  .feature-list svg{position:absolute;left:0;top:2px;width:18px;height:18px}
  .list-left{left:44px;top:733px;width:290px}
  .list-right{left:376px;top:733px;width:310px}
  .list-right li{margin-bottom:14px}
  .divider{position:absolute;left:347px;top:735px;width:2px;height:200px;background:var(--gold)}
  .options{position:absolute;left:108px;top:970px;width:506px;height:186px;border-radius:10px;background:linear-gradient(180deg,#3d9a26,var(--green));padding:24px 18px 0 26px;color:var(--white)}
  .options-head{position:absolute;left:245px;top:950px;width:276px;height:40px;border-radius:20px;background:linear-gradient(180deg,#3a3a3a,var(--charcoal));color:var(--white);font-family:"Oswald",sans-serif;font-weight:500;font-size:27px;text-transform:uppercase;display:flex;align-items:center;justify-content:center;z-index:2}
  .option-row{display:flex;justify-content:space-between;align-items:center;height:26px;font-family:"Oswald",sans-serif;font-size:18px;font-weight:400}
  .option-cost{width:108px;height:20px;background:linear-gradient(180deg,#f2b716,var(--gold-dark));font-size:14px;text-align:center;line-height:20px}
  .website{position:absolute;left:0;right:0;top:1167px;text-align:center;font-weight:700;font-size:17px;color:var(--white)}
</style>
</head>
<body>
<div class="flyer">
  <svg class="backdrop" width="720" height="1200" viewBox="0 0 720 1200" aria-hidden="true">
    <path d="M0,262 C160,262 330,220 440,120 L560,120 L560,575 C380,585 190,560 0,500 Z" fill="var(--gold)"/>
    <path d="M0,276 C170,274 340,236 450,140 L560,140 L560,560 C380,570 190,545 0,480 Z" fill="var(--green)"/>
    <path d="M0,1125 C250,1115 480,1095 720,1060 L720,1200 L0,1200 Z" fill="var(--gold)"/>
    <path d="M0,1140 C250,1132 480,1115 720,1082 L720,1200 L0,1200 Z" fill="var(--gold-dark)" opacity=".55"/>
  </svg>

  <div class="brand"><span class="brand-dot"></span><span class="brand-name">Little Sunroof Builds</span></div>

  <div class="photo photo-hero" role="img" aria-label="Photo of the white board-and-batten tiny trailer house with dark roof, parked outdoors"></div>

  <div class="title">
    <div class="title-lead"><span class="the">The </span><span class="quote">“</span>Prairie Cottage</div>
    <div class="title-main">Mini<span class="quote">”</span></div>
    <div class="subtitle">Luxury, Mobile Vending House</div>
  </div>

  <div class="photo photo-round photo-rear" role="img" aria-label="Photo of the trailer's rear corner with windows and tandem wheels"></div>
  <div class="photo photo-round photo-side" role="img" aria-label="Photo of the trailer's side with serving window and wheels"></div>
  <div class="photo photo-round photo-window" role="img" aria-label="Photo of the serving window being opened on the trailer"></div>

  <div class="pill pill-features">Base Unit Features:</div>
  <div class="pill pill-price">Base Price:<span class="price-tag">$45,000</span></div>

  <ul class="feature-list list-left">
    <li><svg viewBox="0 0 20 20"><circle cx="10" cy="10" r="8" fill="none" stroke="var(--gold)" stroke-width="1.6"/><path d="M6 10l3 3 6-7" fill="none" stroke="var(--gold)" stroke-width="1.8"/></svg>Trailer features tandem wheels w/ brakes</li>
    <li><svg viewBox="0 0 20 20"><circle cx="10" cy="10" r="8" fill="none" stroke="var(--gold)" stroke-width="1.6"/><path d="M6 10l3 3 6-7" fill="none" stroke="var(--gold)" stroke-width="1.8"/></svg>80 gallon water supply tank</li>
    <li><svg viewBox="0 0 20 20"><circle cx="10" cy="10" r="8" fill="none" stroke="var(--gold)" stroke-width="1.6"/><path d="M6 10l3 3 6-7" fill="none" stroke="var(--gold)" stroke-width="1.8"/></svg>100 gallon waste water tank</li>
    <li><svg viewBox="0 0 20 20"><circle cx="10" cy="10" r="8" fill="none" stroke="var(--gold)" stroke-width="1.6"/><path d="M6 10l3 3 6-7" fill="none" stroke="var(--gold)" stroke-width="1.8"/></svg>Cupboards, cabinets &amp; four stainless steel sinks.</li>
    <li><svg viewBox="0 0 20 20"><circle cx="10" cy="10" r="8" fill="none" stroke="var(--gold)" stroke-width="1.6"/><path d="M6 10l3 3 6-7" fill="none" stroke="var(--gold)" stroke-width="1.8"/></svg>60” Gas shock serving window</li>
  </ul>

  <div class="divider"></div>

  <ul class="feature-list list-right">
    <li><svg viewBox="0 0 20 20"><circle cx="10" cy="10" r="8" fill="none" stroke="var(--gold)" stroke-width="1.6"/><path d="M6 10l3 3 6-7" fill="none" stroke="var(--gold)" stroke-width="1.8"/></svg>Steel frame construction for fire retardation safety and weight reduction.</li>
    <li><svg viewBox="0 0 20 20"><circle cx="10" cy="10" r="8" fill="none" stroke="var(--gold)" stroke-width="1.6"/><path d="M6 10l3 3 6-7" fill="none" stroke="var(--gold)" stroke-width="1.8"/></svg>100% off grid with solar and lithium battery system allowing the trailer to be used in places not accessible by traditional trailers.</li>
  </ul>

  <div class="options-head">Available Options:</div>
  <div class="options">
    <div class="option-row"><span>HVAC - Kora Mini Split</span><span class="option-cost">$1,800</span></div>
    <div class="option-row"><span>Cooler / Glass front Commercial refrigerator</span><span class="option-cost">$1,600</span></div>
    <div class="option-row"><span>Upper loft storage area</span><span class="option-cost">$1,200</span></div>
    <div class="option-row"><span>Signage and graphics (depend on complexity)</span><span class="option-cost">$2,000 - $5,000</span></div>
    <div class="option-row"><span>Ice machine</span><span class="option-cost">$1,100</span></div>
  </div>

  <div class="website">www.littlesunroofbuilds.com</div>
</div>
</body>
</html>
```